Building company with a modern and unique product looking for a business card to help us stand out

We currently have a logo but as our business has grown, we feel that our business card is not reflecting our modern and high quality product and help us stand out from the crowd. Our business is mainly in the construction of new homes using a unique method and materials that makes our homes fire proof, vermin and pest resistant and rated to the maximum cyclone category (category 5). We need a business card that helps us stand out as well as communicating professionalism, high quality and trustworthiness. I have attached our current logo with a black and white option, as well as our business card which is double sided. We would like to retain as much of the information that is currently on our business cards, but presented in a more sleek way. We do like our current colour palette ( white, black, yellow and grey) and have been looking primarily at business cards with a black background however we are open to other combinations of colour and layout as long as we stand out. Please feel free to tweak our logo to make it more suitable for a business card, we like the black option that we use but we have had trouble trying to get the white area to match the rest of the logo and blend effectively into a business card. Please do not hesitate to contact us with any questions as we really want this to be successful!

Target Market(s)

Large contracts including government and larger companies

Industry/Entity Type

Business

Contact Information for Business Card

We will be providing this business card to potential clients including key government ministers and large funding companies, our business card should show that we are professional and reliable.

Requirements
Must have
• It must be easy to read and pleasing to the eye, It must contain as much of the information on the current business card and unless something really stands out, we will most likely pick a design that has all of the information included. It must include our logo of course and have some colour included.
Nice to have
• We are looking for a high end business card and would like to see designs that reflect this. We like the gloss/matte contrast, plastic cards with opaque/coloured areas and unique features not seen on everyday paper business cards. It would be nice to see a few different colour combinations, we are open to new ideas so please feel free to take some artistic licence.
Should not have
• Must not be too busy, difficult to read or be distracting from the information conveyed. Other than this please feel free to add your own touches and make it unique!

```html
<!DOCTYPE html>
<html lang="en">
<head>
<meta charset="utf-8">
<title>Korvale Building Company – Business Card</title>
<link rel="stylesheet" href="https://fonts.googleapis.com/css2?family=Open+Sans:wght@400;600;700&display=swap">
<style>
  :root {
    --bg: #d9d9d9;
    --paper: #ffffff;
    --grey: #9c9d9f;
    --ink: #2b2b2b;
    --ink-soft: #555555;
    --black: #1a1a1a;
    --yellow: #f2e600;
  }
  * { box-sizing: border-box; margin: 0; padding: 0; }
  html, body { width: 1200px; height: 900px; overflow: hidden; }
  body {
    background: var(--bg);
    font-family: "Open Sans", Arial, sans-serif;
    color: var(--ink);
    display: flex;
    flex-direction: column;
    align-items: center;
    justify-content: center;
    gap: 44px;
  }
  .card {
    position: relative;
    width: 620px;
    height: 378px;
    background: var(--paper);
    box-shadow: 0 6px 18px rgba(0,0,0,0.18);
    overflow: hidden;
  }

  .brand {
    display: flex;
    align-items: center;
    gap: 10px;
    font-weight: 700;
    color: var(--ink);
    white-space: nowrap;
  }
  .brand__mark {
    width: 14px; height: 14px;
    background: var(--yellow);
    flex: none;
  }

  /* Brand side */
  .card--front .grey-field {
    position: absolute;
    inset: 0;
    background: var(--grey);
    clip-path: polygon(0 46%, 42% 46%, 60% 0, 100% 0, 100% 100%, 0 100%);
  }
  .card--front .brand {
    position: absolute;
    right: 36px;
    top: 128px;
    font-size: 24px;
    color: var(--black);
  }

  /* Contact side */
  .edge-bar {
    position: absolute;
    width: 16px;
    height: 76px;
    background: var(--black);
  }
  .edge-bar--left { left: 0; bottom: 92px; }
  .edge-bar--right { right: 0; top: 30px; }
  .back-body {
    position: absolute;
    left: 58px; top: 72px;
    display: flex;
    align-items: center;
    gap: 20px;
  }
  .card--back .brand { font-size: 16px; }
  .divider {
    width: 1px; height: 112px;
    background: var(--ink-soft);
  }
  .contact { white-space: nowrap; }
  .contact__name { font-size: 16px; font-weight: 700; }
  .contact__role { font-size: 11px; color: var(--ink-soft); margin-bottom: 10px; }
  .contact__list { list-style: none; font-size: 13px; line-height: 1.7; }
  .contact__list li { display: flex; align-items: center; gap: 8px; }
  .contact__list svg { width: 14px; height: 14px; flex: none; }
  .tagline {
    position: absolute;
    left: 58px; right: 40px; bottom: 50px;
    font-size: 15px;
    line-height: 1.45;
  }
  .features { display: flex; gap: 14px; list-style: none; }
  .features li { display: flex; align-items: center; gap: 5px; }
  .tick { width: 13px; height: 13px; flex: none; }
</style>
</head>
<body>

  <section class="card card--back" aria-label="Business card, contact side">
    <span class="edge-bar edge-bar--left"></span>
    <span class="edge-bar edge-bar--right"></span>

    <div class="back-body">
      <div class="brand"><span class="brand__mark"></span>Korvale Building Company</div>
      <span class="divider"></span>
      <div class="contact">
        <p class="contact__name">Callum Reyes</p>
        <p class="contact__role">Managing Director</p>
        <ul class="contact__list">
          <li><svg viewBox="0 0 14 14"><rect x="3" y="1" width="8" height="12" rx="1.5" fill="var(--black)"/><rect x="4.5" y="3" width="5" height="6" fill="#fff"/></svg>: 0400 123 987</li>
          <li><svg viewBox="0 0 14 14"><path d="M2 4c0-2 3-2 3 0l-1 2c1 2 2 3 4 4l2-1c2 0 2 3 0 3C6 12 2 8 2 4z" fill="var(--black)"/></svg>: (02) 5550 1844</li>
          <li><svg viewBox="0 0 14 14"><rect x="1" y="3" width="12" height="8" fill="var(--black)"/><path d="M1 3l6 5 6-5" stroke="#fff" fill="none"/></svg>: hello@korvalebuilding.com</li>
        </ul>
      </div>
    </div>

    <div class="tagline">
      <p>Specializing in Homes that are</p>
      <ul class="features">
        <li><svg class="tick" viewBox="0 0 13 13"><rect width="13" height="13" fill="var(--black)"/><path d="M3 7l2.5 2.5L10 4" stroke="var(--yellow)" stroke-width="2" fill="none"/></svg>Fire Proof</li>
        <li><svg class="tick" viewBox="0 0 13 13"><rect width="13" height="13" fill="var(--black)"/><path d="M3 7l2.5 2.5L10 4" stroke="var(--yellow)" stroke-width="2" fill="none"/></svg>Climate Proof</li>
        <li><svg class="tick" viewBox="0 0 13 13"><rect width="13" height="13" fill="var(--black)"/><path d="M3 7l2.5 2.5L10 4" stroke="var(--yellow)" stroke-width="2" fill="none"/></svg>Cyclone Rated (Cat. 5)</li>
      </ul>
    </div>
  </section>

  <section class="card card--front" aria-label="Business card, brand side">
    <div class="grey-field"></div>
    <div class="brand"><span class="brand__mark"></span>Korvale Building Company</div>
  </section>

</body>
</html>
```